QLENT Website Redesign - More modern look & feel

I will upload high resolution copies of the QLENT logo tomorrow
Please make website responsive/mobile friendly
Use simple and clean black & white, easy to read text, color transitions & translucent, shadows, reflections/metallic
Alternate between white and black backgrounds from section to section but start with white background at top of fold/hero section
Freeze top bar & change to dark when scrolling down
If possible, have site convert to black background when consumer using dark mode on their phone or browser
Use high quality images of various types of business payments, in-store and online
Make sure photos are inclusive of race & sex/gender and show payments & business interaction
Use a high quality image of a website payment checkout screen
Use clear banner for logos under hero section
CTA at each section (bold caps with bright green)
Use only one shade of green
Use consistent font/text
Use Qlent building image at bottom in get started section
Target Market(s)
US businesses
Industry/Entity Type
Fintech (financial technology) / merchant services
Number of Pages Required
1 page
Look and feel

```html
<!DOCTYPE html>
<html lang="en">
<head>
<meta charset="utf-8">
<title>QLENT — Payments Simplified</title>
<link rel="stylesheet" href="https://fonts.googleapis.com/css2?family=Poppins:wght@500;600;700&family=Roboto:wght@400;500;700&display=swap">
<style>
  :root {
    --white: #ffffff;
    --off-white: #f3f5f4;
    --black: #0b0d0c;
    --ink: #121614;
    --muted: #5b6662;
    --line: #d9dedc;
    --green: #14d477;
  }
  * { box-sizing: border-box; margin: 0; padding: 0; }
  html, body { width: 1200px; height: 585px; overflow: hidden; }
  body {
    position: relative;
    background: var(--white);
    font-family: "Roboto", Arial, sans-serif;
    color: var(--ink);
  }
  .hero-section {
    position: absolute; left: 0; top: 0; width: 1200px; height: 505px;
    background: linear-gradient(180deg, var(--white) 0%, var(--off-white) 100%);
  }
  .top-phone {
    position: absolute; top: 13px; left: 0; width: 100%;
    text-align: center; font-size: 6.5px; font-weight: 700; color: var(--green);
    letter-spacing: 0.2px;
  }
  .site-nav { position: absolute; top: 44px; left: 0; width: 100%; height: 16px; }
  .brand {
    position: absolute; left: 378px; top: 1px;
    font-family: "Poppins", sans-serif; font-weight: 600; font-size: 9.5px; letter-spacing: 3px;
    color: var(--ink);
  }
  .nav-pill {
    position: absolute; top: 0; height: 15px;
    border: 1px solid var(--ink); border-radius: 8px; color: var(--ink);
    font-family: "Poppins", sans-serif; font-weight: 600; font-size: 6px;
    display: flex; align-items: center; justify-content: center; letter-spacing: -0.1px;
  }
  .nav-pill.cta {
    top: 1px; height: 13px;
    background: var(--green); border-color: var(--green); color: var(--black); font-weight: 700; letter-spacing: 0.3px; font-size: 5.5px;
  }
  .hero-panel {
    position: absolute; left: 169px; top: 132px; width: 863px; height: 217px;
    border-radius: 10px;
    background: linear-gradient(180deg, rgba(255,255,255,0.9) 0%, rgba(232,236,234,0.95) 100%);
    border: 1px solid var(--line);
    box-shadow: 0 14px 34px rgba(0,0,0,0.10), 0 2px 6px rgba(0,0,0,0.05);
  }
  .hero-visual {
    position: absolute; left: 377px; top: 150px; width: 224px; height: 180px;
    background: linear-gradient(160deg, #eef1f0 0%, #d5dbd8 100%);
    border-radius: 6px;
  }
  .hero-copy { position: absolute; left: 632px; top: 172px; }
  .hero-title { font-size: 19px; font-weight: 400; color: var(--green); }
  .hero-title strong { color: var(--ink); font-weight: 700; }
  .hero-sub { margin-top: 11px; font-size: 11.5px; color: var(--muted); }
  .hero-sub strong, .hero-points strong { color: var(--green); font-weight: 700; }
  .hero-points { margin-top: 13px; font-size: 11px; font-weight: 500; line-height: 14px; color: var(--muted); }
  .hero-points .plus { color: var(--ink); font-weight: 700; }
  .hero-actions { margin-top: 20px; display: flex; align-items: center; gap: 8px; }
  .btn-start {
    width: 78px; height: 25px; border: 1px solid var(--ink); border-radius: 13px; padding: 2px;
  }
  .btn-start span {
    display: flex; align-items: center; justify-content: center; width: 100%; height: 100%;
    border-radius: 11px; background: var(--green); color: var(--black);
    font-family: "Poppins", sans-serif; font-weight: 700; font-size: 5px; letter-spacing: 1.2px;
  }
  .hero-actions .note { font-family: "Poppins", sans-serif; font-size: 8px; font-weight: 600; color: var(--ink); }
  .solutions-section {
    position: absolute; left: 0; top: 505px; width: 1200px; height: 80px;
    background: var(--black);
  }
  .section-label {
    position: absolute; left: 529px; top: 32px; width: 82px; height: 30px;
    border: 1px solid var(--white); border-radius: 10px; color: var(--white);
    display: flex; align-items: center; justify-content: center;
    font-family: "Poppins", sans-serif; font-weight: 700; font-size: 11px;
  }
</style>
</head>
<body>
  <section class="hero-section">
    <div class="top-phone">(555-013-2468)</div>

    <nav class="site-nav">
      <div class="brand">QLENT</div>
      <a class="nav-pill" style="left:455px;width:45px">SOLUTIONS</a>
      <a class="nav-pill" style="left:543px;width:34px">PRICING</a>
      <a class="nav-pill" style="left:620px;width:38px">CONTACT</a>
      <a class="nav-pill" style="left:700px;width:28px">LOGIN</a>
      <a class="nav-pill cta" style="left:773px;width:50px">GET STARTED</a>
    </nav>

    <div class="hero-panel"></div>
    <div class="hero-visual" role="img" aria-label="Line illustration of a laptop showing the QLENT name beside a card payment terminal"></div>
    <div class="hero-copy">
      <h1 class="hero-title">Payments <strong>Simplifield.</strong></h1>
      <p class="hero-sub">Accept Payments <strong>Your Way</strong></p>
      <p class="hero-points">Transparent <strong>Pricing</strong><span class="plus">+</span> Quick &amp; Easy<br><strong>Setup</strong> For All Types Of Businesses</p>
      <div class="hero-actions">
        <a class="btn-start"><span>GET STARTED</span></a>
        <span class="note">Free To Get Started</span>
      </div>
    </div>
  </section>

  <section class="solutions-section">
    <div class="section-label">SOLUTIONS</div>
  </section>
</body>
</html>
```